Brivonex Letter head

Brivonex is a young and energetic software development consultancy. We spend our time working with clients to turn what ever is in their heads in to software.
We are trying to create an image of a high class software boutique who build class leading bespoke solutions.
We need a sharp letter head that looks great on high quality media.
We like bold colours and distinctive design. So show us what you can do.
Industry/Entity Type
Software
Requirements
Must have
- Our company is based in the UK and are requried to have on the paper somewhere the following information:
* Registered company name: Brivonex Ltd
* Registered company number
* VAT registration number
In addition we also want the following:
* An email address
* Telephone number
* Website address
An example of what some pages have in their footer is something like the following:
Brivonex Ltd is registered in England and Wales. Reg. no: 5316240
Registered office: 41 Pellowmore Road, Hartcombe Middlesex, HC47QD. Tel: 07812365091
You do not have to use this sentance but please make sure your design incorporates accommodates the requirements for UK based companies

```html
<!DOCTYPE html>
<html lang="en">
<head>
<meta charset="utf-8">
<title>Brivonex Letterhead</title>
<link rel="stylesheet" href="https://fonts.googleapis.com/css2?family=Source+Sans+3:wght@400;600&display=swap">
<style>
  :root {
    --brand-red: #c8202f;
    --brand-red-deep: #8e0f1a;
    --brand-red-bright: #e3222b;
    --ink: #3c3c3c;
    --rule: #c9c9c9;
    --paper: #ffffff;
    --steel-dark: #7d7d7d;
    --steel-light: #e2e2e2;
  }
  html, body {
    margin: 0;
    padding: 0;
    width: 986px;
    height: 1200px;
    overflow: hidden;
    background: var(--paper);
  }
  .letterhead {
    position: relative;
    width: 986px;
    height: 1200px;
    background: var(--paper);
    font-family: "Source Sans 3", sans-serif;
    color: var(--ink);
  }
  .brand {
    position: absolute;
    left: 52px;
    top: 36px;
    margin: 0;
    font-size: 62px;
    font-weight: 400;
    letter-spacing: 2px;
    line-height: 1;
    color: var(--brand-red);
  }
  .company-details {
    position: absolute;
    right: 226px;
    top: 36px;
    margin: 0;
    text-align: right;
    font-style: normal;
    font-size: 16px;
    line-height: 19px;
  }
  .company-details .strong { font-weight: 600; }
  .divider {
    position: absolute;
    left: 779px;
    top: 33px;
    width: 1px;
    height: 80px;
    background: var(--rule);
  }
  .contact-list {
    position: absolute;
    left: 792px;
    top: 36px;
    margin: 0;
    padding: 0;
    list-style: none;
    font-size: 16px;
    line-height: 27px;
  }
  .contact-list li {
    display: flex;
    align-items: center;
    gap: 8px;
  }
  .contact-list svg { width: 15px; height: 15px; flex: none; }
  .footer-band {
    position: absolute;
    left: 0;
    bottom: 0;
    width: 986px;
    height: 40px;
  }
  .footer-text {
    position: absolute;
    left: 594px;
    bottom: 11px;
    margin: 0;
    font-size: 15px;
    color: #ffffff;
    white-space: nowrap;
  }
</style>
</head>
<body>
<main class="letterhead">
  <header>
    <h1 class="brand">BRIVONEX</h1>
    <address class="company-details">
      <span class="strong">Brivonex Ltd</span><br>
      <span class="strong">Registered: England &amp; Wales</span><br>
      41 Pellowmore Road<br>
      Hartcombe Middlesex, HC47QD
    </address>
    <div class="divider"></div>
    <ul class="contact-list">
      <li>
        <svg viewBox="0 0 16 16" aria-hidden="true">
          <circle cx="8" cy="8" r="7" fill="none" stroke="var(--brand-red)" stroke-width="1.4"/>
          <path d="M6 4.5c-.8.6-1 1.8-.4 3.3.6 1.6 1.8 3 3 3.7.7.3 1.3.2 1.8-.3l-1.2-1.3-.8.5c-.8-.5-1.5-1.4-1.8-2.3l.7-.6-.9-1.6z" fill="var(--brand-red)"/>
        </svg>
        07812365091
      </li>
      <li>
        <svg viewBox="0 0 16 16" aria-hidden="true">
          <path d="M1.5 6 8 2l6.5 4v7.5h-13z" fill="var(--brand-red)"/>
          <path d="M3.5 6.5h9v3L8 12 3.5 9.5z" fill="#ffffff"/>
        </svg>
        info@brivonex.com
      </li>
      <li>
        <svg viewBox="0 0 16 16" aria-hidden="true">
          <g fill="none" stroke="var(--brand-red)" stroke-width="1.1">
            <circle cx="8" cy="8" r="6.5"/>
            <ellipse cx="8" cy="8" rx="3" ry="6.5"/>
            <path d="M1.5 8h13M2.5 4.8h11M2.5 11.2h11"/>
          </g>
        </svg>
        www.brivonex.com
      </li>
    </ul>
  </header>

  <footer>
    <svg class="footer-band" viewBox="0 0 986 40" aria-hidden="true">
      <defs>
        <linearGradient id="steel" x1="0" x2="1" y1="0" y2="0">
          <stop offset="0" stop-color="var(--steel-dark)"/>
          <stop offset="1" stop-color="var(--steel-light)"/>
        </linearGradient>
        <linearGradient id="redband" x1="0" x2="1" y1="0" y2="0">
          <stop offset="0" stop-color="var(--brand-red-bright)"/>
          <stop offset="1" stop-color="var(--brand-red-deep)"/>
        </linearGradient>
      </defs>
      <polygon points="0,20 492,20 474,40 0,40" fill="url(#steel)"/>
      <polygon points="529,0 986,0 986,40 486,40" fill="url(#redband)"/>
    </svg>
    <p class="footer-text">Reg. no: 5316240 &nbsp;|&nbsp; VAT Reg. no: 5316240</p>
  </footer>
</main>
</body>
</html>
```